Thoroughbred Racing Partnership needs web design

Crown of Laurels Partners is a management group who buys horses and races them on both the West and East coasts. The premise of the business is for an investment as little as $500, anyone can be a partner and own a percentage of a horse(s). This is a low cost way of getting involved in the exciting sport of Thoroughbred Racing, without shouldering the heavy financial responsibility. Our target market is mostly males 40+ but we want to include all target markets. We are looking for something very clean and professional, we want to give an image of success. Nothing overly "artsy." I have included the logo in which you can incorporate in the site. Also, the logo colors will be the colors of our "silks." The silks are what the jockey wears and will be an important marketing tool for COL. We would like a very prominent picture of a racehorse somewhere on the homepage, we want to make it clear that is a website for Horseracing partnerships.

On the top of the site, it should say "Crown of Laurels" (on the top)
and below that "Thoroughbred Racing Partnerships." (below that)

The main sections, which should be across the top are:

Home
About Us
Ownership
Stable Roster
News
Contact us

Some of these will have drop down menus.

An example of a competitor website that we like is: www.harrowfieldstable.example
An example of a competitor website that we don't like is: www.gallopmarket.example
Updates

Project Deadline Extended
Reason: We have a Board of Directors meeting on the 22nd and we will be making a decision on that day. I'm giving an extension so that all designers are able to submit their designs by the 22nd. Thank you!

Target Market(s)

40+ males

Industry/Entity Type

Business

Requirements
Must have
• our logo must be on the site. We would like at least one bold image of a thoroughbred horse in action. The picture is going to tell the story so it needs to be very eye-catching.

Our slogan should also be included on the website, "Experience the thrill of owning a Racehorse."
Should not have
• cartoons, artsy pictures, pictures of Steeplechase horses or "jumpers." This partnership is for racehorses only, there is not jumping involved with the horses.

```html
<!DOCTYPE html>
<html lang="en">
<head>
<meta charset="utf-8">
<title>Crown of Laurels – Thoroughbred Racing Partnerships</title>
<link href="https://fonts.googleapis.com/css2?family=Source+Sans+3:wght@300;400;600&family=Fira+Sans+Extra+Condensed:wght@400;700&family=Noto+Serif:wght@400&display=swap" rel="stylesheet">
<style>
:root{
  --navy:#0b3a6b;
  --navy-dark:#062a52;
  --blue:#1d5b94;
  --blue-text:#1f5890;
  --ink:#2a2a2a;
  --grey:#5a5a5a;
  --rule:#d8d8d8;
  --white:#ffffff;
}
*{box-sizing:border-box;margin:0;padding:0}
html,body{width:1182px;height:1200px;overflow:hidden;background:var(--white)}
body{position:relative;font-family:"Source Sans 3",sans-serif;color:var(--ink)}
.topbar{position:absolute;left:0;top:0;width:1182px;height:90px;background:linear-gradient(#0a3c70,#06305d)}
.utility{position:absolute;right:96px;top:11px;font:400 12px "Fira Sans Extra Condensed",sans-serif;color:var(--white);letter-spacing:.3px}
.utility span{margin:0 6px;opacity:.8}
.hero{position:absolute;left:0;top:90px;width:1182px;height:546px;background:
 radial-gradient(ellipse at 25% 40%,rgba(200,40,50,.55),transparent 40%),
 radial-gradient(ellipse at 20% 85%,rgba(200,150,40,.7),transparent 35%),
 linear-gradient(100deg,#5b4a32 0%,#7a6440 30%,#4a3020 55%,#8a5a3a 75%,#3a2a22 100%);border-bottom:2px solid #1a1a1a}
.header{position:absolute;left:86px;top:41px;width:1008px;height:103px;background:linear-gradient(#ffffff,#dfe8f1);border:1px solid #c8d4e0;box-shadow:0 2px 6px rgba(0,0,0,.25)}
.brand-mark{position:absolute;left:28px;top:38px;display:flex;align-items:center;gap:7px;font:600 17px "Source Sans 3",sans-serif;color:var(--navy)}
.brand-mark i{width:14px;height:14px;border-radius:50%;background:var(--navy);display:block}
.site-title{position:absolute;left:175px;top:28px;font:400 23px "Noto Serif",serif;color:var(--navy-dark);letter-spacing:.2px;white-space:nowrap}
.site-sub{position:absolute;left:178px;top:60px;font:400 16px "Source Sans 3",sans-serif;color:var(--navy-dark)}
.nav{position:absolute;right:14px;top:37px;display:flex;font:400 17px "Fira Sans Extra Condensed",sans-serif;color:var(--navy-dark)}
.nav a{display:block;padding:5px 12px;text-decoration:none;color:inherit}
.nav a.active{background:var(--blue);color:var(--white);border-radius:2px;padding:5px 14px;margin-right:5px}
.slogan{position:absolute;left:92px;top:364px;font:700 48px/48px "Fira Sans Extra Condensed",sans-serif;color:var(--white);text-transform:uppercase;text-shadow:1px 2px 3px rgba(0,0,0,.5)}
.slider-btn{position:absolute;left:92px;top:565px;width:49px;height:49px;border-radius:50%;background:rgba(255,255,255,.85)}
.video{position:absolute;left:648px;top:286px;width:423px;height:264px;background:#111}
.video-frame{position:absolute;left:0;top:0;width:423px;height:236px;background:linear-gradient(90deg,#3a4a60,#1c1d22 40%,#242838)}
.video-title{position:absolute;left:12px;top:7px;font:400 13px "Source Sans 3",sans-serif;color:#eee}
.video-bar{position:absolute;left:0;top:236px;width:423px;height:28px;background:linear-gradient(#2c2c2c,#161616)}
.video-time{position:absolute;left:94px;top:7px;font:400 11px "Source Sans 3",sans-serif;color:#ddd}
.content h2{font:400 26px "Source Sans 3",sans-serif;color:var(--blue-text)}
.intro{position:absolute;left:88px;top:686px;width:470px}
.intro h1{font:400 28px "Source Sans 3",sans-serif;color:var(--ink);margin-bottom:10px;white-space:nowrap}
.intro .lead{font:300 16px/23px "Source Sans 3",sans-serif;color:var(--grey);margin-bottom:12px}
.intro p{font:300 14px/22px "Source Sans 3",sans-serif;color:var(--grey);margin-bottom:9px}
.roster{position:absolute;left:571px;top:688px;width:248px}
.roster-photo{width:248px;height:105px;margin:10px 0 8px;background:linear-gradient(120deg,#2f5a9a 0%,#c23a3a 35%,#8a4a2a 60%,#a06a40 100%)}
.roster h3{font:400 16px "Source Sans 3",sans-serif;color:var(--blue-text);margin-bottom:4px}
.roster p{font:300 14px/19px "Source Sans 3",sans-serif;color:var(--grey)}
.btn{display:inline-block;margin-top:10px;padding:5px 14px;background:linear-gradient(#2a6aa8,#0c3d72);color:var(--white);font:400 14px "Source Sans 3",sans-serif;border-radius:3px;box-shadow:0 1px 2px rgba(0,0,0,.4)}
.news{position:absolute;left:852px;top:688px;width:250px}
.news ul{list-style:none;margin-top:8px}
.news li{padding-bottom:6px;margin-bottom:8px;border-bottom:1px solid var(--rule)}
.news li:last-of-type{border-bottom:0;margin-bottom:0}
.news-title{display:block;font:400 15px "Source Sans 3",sans-serif;color:var(--ink)}
.news-text{font:400 14px "Source Sans 3",sans-serif;color:#444}
.footer{position:absolute;left:0;top:984px;width:1182px;height:216px;background:linear-gradient(#e7ecf2,#fbfcfd 60%);border-top:1px solid #dfe4ea}
.footer .col{position:absolute;top:32px;font:300 14px/23px "Source Sans 3",sans-serif;color:var(--blue-text)}
.footer h4{font:400 19px "Source Sans 3",sans-serif;color:var(--blue-text);margin-bottom:6px;margin-top:-3px}
.footer .name{font-size:16px}
.social{display:flex;gap:10px;margin-top:14px}
.social i{display:block;width:23px;height:23px;border-radius:2px}
.links ul{list-style:none}
.links li::before{content:"";display:inline-block;border-left:5px solid #a8b6c6;border-top:4px solid transparent;border-bottom:4px solid transparent;margin-right:9px}
.foot-mark{position:absolute;left:888px;top:70px;display:flex;align-items:center;gap:8px;font:600 24px "Source Sans 3",sans-serif;color:var(--navy)}
.foot-mark i{width:20px;height:20px;border-radius:50%;background:var(--navy);display:block}
</style>
</head>
<body>
<div class="topbar"><div class="utility">LOGIN<span>|</span>SUPPORT<span>|</span>SIGN UP</div></div>
<div class="hero" role="img" aria-label="Photo of thoroughbred racehorses with jockeys in silks galloping on the track"></div>
<header class="header">
  <div class="brand-mark"><i></i>COL PARTNERS</div>
  <div class="site-title">CROWN OF LAURELS</div>
  <div class="site-sub">Thoroughbred Racing Partnerships</div>
  <nav class="nav"><a class="active">HOME</a><a>ABOUT US</a><a>OWNERSHIP</a><a>STABLE ROSTER</a><a>NEWS</a><a>CONTACT US</a></nav>
</header>
<div class="slogan">Experience the thrill<br>of owning a racehorse</div>
<div class="slider-btn"><svg width="49" height="49" viewBox="0 0 49 49"><path d="M21 17l-7 7.5 7 7.5M28 17l7 7.5-7 7.5" fill="none" stroke="#4a5a6a" stroke-width="2"/></svg></div>
<div class="video">
  <div class="video-frame" role="img" aria-label="Video still of three partners holding a racing award plaque"></div>
  <div class="video-title">How We Buy a Racehorse for Harrowfield Thoroughb...</div>
  <svg style="position:absolute;right:12px;top:8px" width="44" height="16"><circle cx="4" cy="8" r="2" fill="#eee"/><circle cx="12" cy="3" r="2" fill="#eee"/><circle cx="12" cy="13" r="2" fill="#eee"/><path d="M4 8L12 3M4 8l8 5" stroke="#eee" stroke-width="1.5"/><circle cx="35" cy="8" r="7" fill="#eee"/><rect x="34" y="6" width="2" height="6" fill="#111"/></svg>
  <div class="video-bar">
    <svg style="position:absolute;left:0;top:-6px" width="423" height="34"><rect x="0" y="4" width="423" height="4" fill="#444"/><circle cx="10" cy="6" r="5" fill="#ddd"/><path d="M22 16l11 6-11 6z" fill="#ccc"/><path d="M62 18h4l5-4v16l-5-4h-4z" fill="#ccc"/><circle cx="329" cy="22" r="5" fill="#aaa"/><path d="M405 16h-4v4M413 16h4v4M405 28h-4v-4M413 28h4v-4" stroke="#ccc" stroke-width="1.5" fill="none"/></svg>
    <div class="video-time">00:00 / 11:49</div>
  </div>
</div>
<main class="content">
  <section class="intro">
    <h1>Duis tincidunt lectus quis dui viverra</h1>
    <p class="lead">Mauris vel lacus vitae felis vestibulum volutpat. Etiam est nunc, venenatis in, tristique eu, imperdiet ac, nisl.</p>
    <p>Mauris vel lacus vitae felis vestibulum volutpat. Etiam est nunc, venenatis in, tristique eu, imperdiet ac, nisl. Cum sociis natoque penatibus et magnis dis parturient montes, nascetur ridiculus mus. In iaculis facilisis massa.</p>
    <p>Etiam eu urna. Sed porta. Suspendisse quam leo, molestie sed, luctus quis, feugiat in, pede. Fusce tellus.</p>
  </section>
  <section class="roster">
    <h2>Stable Rosters</h2>
    <div class="roster-photo" role="img" aria-label="Photo of a jockey in red silks riding a chestnut racehorse"></div>
    <h3>Mauris vel lacus vitae felis</h3>
    <p>Etiam est nunc, venenatis in, tristique eu, imperdiet ac nisl. Cum sociis</p>
    <a class="btn">View More</a>
  </section>
  <section class="news">
    <h2>Latest News</h2>
    <ul>
      <li><b class="news-title">Phasellus felis dolor</b><span class="news-text">Dictum dolor eu dictum porttitor enim felis</span></li>
      <li><b class="news-title">Aliquam nec erat at purus</b><span class="news-text">Dictum dolor eu dictum porttitor enim felis</span></li>
      <li><b class="news-title">Nunc porta convallis pede</b><span class="news-text">Dictum dolor eu dictum porttitor enim felis</span></li>
    </ul>
    <a class="btn">View More News</a>
  </section>
</main>
<footer class="footer">
  <div class="col" style="left:91px;top:36px">Copyright © 2013 Crown of Laurels.<br>All rights reserved. Site Map · Contact Us
    <div class="social"><i style="background:#3b5b98"></i><i style="background:#45b0e0"></i><i style="background:#1a73a8"></i><i style="background:#f07c22"></i></div>
  </div>
  <div class="col" style="left:372px"><h4>Contact Information</h4><span class="name">Crown of Laurels</span><br>48 Meadowrun Lane #4B<br>Millbrook 12545 NY<br>Phone +1 (555) 014-2290<br>Email add: info@colpartners.example</div>
  <div class="col links" style="left:584px"><h4>Quick Links</h4><ul><li>Home</li><li>About Us</li><li>Ownership</li></ul></div>
  <div class="col links" style="left:732px;top:60px"><ul><li>Stable Roster</li><li>News</li><li>Contact us</li></ul></div>
  <div class="foot-mark"><i></i>COL PARTNERS</div>
</footer>
</body>
</html>
```